Business card design for upmarket Home Technology design and Installation company

Hello designers, we need a great business card designed.
We need it to convey high tech, and also sophistication .
We work with some of the most affluent people in the world building them home technology systems, and A/V entertainment systems.

Services offered include the following:
Design, sales, installation, and maintenance of

*Home Automation systems
*Distributed / Multi-Room Audio and Video
*High Performance Networks & WiFi
* Lighting and Shade Control
*Home cinema
*Security and CCTV Systems

I have included a copy of our logo to use for your design efforts.

Target Market(s)

Upmarket clients with multi million euro villas.

Industry/Entity Type

Home technology

Contact Information for Business Card

NAME: Derek Halvin ADDRESS: Carrer Bellamar Local 42, Cala Torrent, 07293 PHONE: +34-652-918-204 EMAIL: DHalvin@VORTELhomesystems.example WEB: www.vortelhomesystems.example

Requirements
Must have
• Our Logo, and our tagline

```html
<!DOCTYPE html>
<html lang="en">
<head>
<meta charset="utf-8">
<title>VORTEL – Business Card</title>
<link rel="stylesheet" href="https://fonts.googleapis.com/css2?family=Poppins:wght@400;500;600&display=swap">
<style>
  :root {
    --backdrop: #1c1c1c;
    --card: #101010;
    --gold: #c9a24f;
    --gold-light: #f3d795;
    --gold-dark: #9c7830;
    --ink-light: #f2f2f2;
  }
  * { box-sizing: border-box; margin: 0; padding: 0; }
  html, body { width: 1200px; height: 900px; overflow: hidden; }
  body {
    background: var(--backdrop);
    font-family: "Poppins", sans-serif;
    display: flex;
    flex-direction: column;
    align-items: center;
    justify-content: center;
    gap: 36px;
  }
  .card {
    position: relative;
    width: 700px;
    height: 400px;
    background: var(--card);
    overflow: hidden;
    box-shadow: 0 14px 30px rgba(0,0,0,.55);
  }

  /* Front */
  .brand-name {
    position: absolute;
    top: 42px;
    right: 120px;
    font-size: 72px;
    font-weight: 500;
    letter-spacing: 14px;
    color: var(--gold);
    line-height: 1;
  }
  .tagline {
    position: absolute;
    top: 150px;
    left: 70px;
    font-size: 21px;
    color: var(--gold);
    letter-spacing: .5px;
  }
  .services {
    position: absolute;
    top: 186px;
    left: 70px;
    list-style: none;
  }
  .services li {
    display: flex;
    align-items: center;
    gap: 12px;
    font-size: 19px;
    line-height: 25px;
    color: var(--ink-light);
  }
  .services li::before {
    content: "";
    width: 11px;
    height: 11px;
    border-radius: 50%;
    background: var(--gold);
    flex: none;
  }
  .gold-rule {
    position: absolute;
    left: 0; right: 0; bottom: 0;
    height: 12px;
    background: linear-gradient(90deg, var(--gold-dark), var(--gold-light), var(--gold));
  }

  /* Back */
  .holder-name {
    position: absolute;
    top: 56px;
    left: 56px;
    font-size: 28px;
    font-weight: 600;
    letter-spacing: 1px;
    text-transform: uppercase;
    color: var(--gold);
  }
  .address {
    position: absolute;
    top: 168px;
    left: 56px;
    width: 300px;
    font-size: 18px;
    line-height: 25px;
    color: var(--gold);
  }
  .contacts {
    position: absolute;
    top: 268px;
    left: 56px;
    list-style: none;
    z-index: 1;
  }
  .contacts li {
    display: flex;
    align-items: center;
    gap: 8px;
    font-size: 17px;
    line-height: 28px;
    color: var(--gold);
    white-space: nowrap;
  }
  .contacts svg { width: 17px; height: 17px; flex: none; }
  .accent-disc {
    position: absolute;
    right: -60px;
    bottom: -90px;
    width: 300px;
    height: 300px;
  }
</style>
</head>
<body>

<section class="card card-front">
  <div class="brand-name">VORTEL</div>
  <p class="tagline">Design, sales, installation and maintenance of</p>
  <ul class="services">
    <li>Home Automation systems</li>
    <li>Distributed / Multi-Room Audio and Video</li>
    <li>High Performance Networks &amp; WiFi</li>
    <li>Lighting and Shade Control</li>
    <li>Home cinema</li>
    <li>Security and CCTV Systems</li>
  </ul>
  <div class="gold-rule"></div>
</section>

<section class="card card-back">
  <h1 class="holder-name">Derek Halvin</h1>
  <p class="address">Carrer Bellamar Local 42,<br>Cala Torrent, 07293</p>
  <ul class="contacts">
    <li>
      <svg viewBox="0 0 24 24" fill="var(--gold)"><path d="M6.6 10.8a15.1 15.1 0 0 0 6.6 6.6l2.2-2.2c.3-.3.7-.4 1-.2 1.1.4 2.3.6 3.6.6.6 0 1 .4 1 1V20c0 .6-.4 1-1 1C10.6 21 3 13.4 3 4c0-.6.4-1 1-1h3.5c.6 0 1 .4 1 1 0 1.3.2 2.5.6 3.6.1.3 0 .7-.2 1z"/></svg>
      +34-652-918-204
    </li>
    <li>
      <svg viewBox="0 0 24 24" fill="var(--gold)"><path d="M3 5h18v14H3z M3 5l9 7 9-7" stroke="var(--card)" stroke-width="1.6"/></svg>
      www.vortelhomesystems.example
    </li>
    <li>
      <svg viewBox="0 0 24 24" fill="none" stroke="var(--gold)" stroke-width="1.8"><circle cx="12" cy="12" r="9"/><ellipse cx="12" cy="12" rx="4" ry="9"/><path d="M3 12h18"/></svg>
      DHalvin@VORTELhomesystems.example
    </li>
  </ul>
  <svg class="accent-disc" viewBox="0 0 300 300" aria-hidden="true">
    <defs>
      <linearGradient id="discGold" x1="0" y1="0" x2="1" y2="1">
        <stop offset="0" stop-color="#9c7830"/>
        <stop offset=".55" stop-color="#c9a24f"/>
        <stop offset="1" stop-color="#f3d795"/>
      </linearGradient>
    </defs>
    <circle cx="150" cy="150" r="150" fill="url(#discGold)"/>
  </svg>
</section>

</body>
</html>
```